Design revision of an existing Executive Summary

Our company velnova is specialized in the field of performance engineering (load and performance testing as well as application performance monitoring). We are looking for a designer who could graphically "spice up" our current executive summary about our company velnova (www.velnova-ops.com). Maybe it would be possible to incorporate a pic of our website (e.g. https://www.velnova-ops.com/en/services/performance/) into this newly designed executive summary.

Attached you will find the current executive summary which should not change textually. It should just look fresher and more modern. Ideally, a visually appealing first / title page would precede the text.

```html
<!DOCTYPE html>
<html lang="en">
<head>
<meta charset="utf-8">
<title>velnova – Executive Summary Brochure</title>
<link href="https://fonts.googleapis.com/css2?family=Montserrat:wght@400;600;700&family=Open+Sans:wght@400;600&display=swap" rel="stylesheet">
<style>
  :root{
    --bg:#e1e2e4;
    --panel-dark:#1b1d22;
    --panel-mid:#24272d;
    --blue:#2456b5;
    --blue-bright:#3d7ee6;
    --blue-deep:#17367a;
    --text-light:#ffffff;
    --text-muted:#a7abb3;
    --text-soft:#c9ccd2;
    --card:#3a3d44;
  }
  *{margin:0;padding:0;box-sizing:border-box}
  html,body{width:1200px;height:2776px;overflow:hidden;background:var(--bg)}
  body{position:relative;font-family:"Open Sans",Arial,sans-serif;color:var(--text-light)}
  .spread{position:absolute;left:76px;width:1048px;display:grid;grid-template-columns:repeat(3,1fr);box-shadow:0 6px 24px rgba(0,0,0,.18)}
  .spread--inside{top:622px;height:700px}
  .spread--outside{top:1402px;height:752px}
  .panel{position:relative;overflow:hidden;background:var(--panel-dark)}
  .photo{position:absolute;left:0;right:0}
  .heading{font-family:"Montserrat",Arial,sans-serif;font-weight:700;font-size:26px;line-height:1.15;letter-spacing:1px;text-transform:uppercase;color:var(--text-light)}
  .heading-bar{display:block;width:46px;height:4px;background:var(--blue-bright);margin-top:10px}
  .sub{font-family:"Montserrat",Arial,sans-serif;font-weight:600;font-size:11px;color:var(--blue-bright);margin-bottom:6px}
  .body{font-size:10px;line-height:1.55;color:var(--text-muted)}
  .block{position:absolute;left:32px;right:32px}

  /* inside: services */
  .services .photo{top:0;height:150px;background:linear-gradient(180deg,#3b4350 0%,#2a2e36 60%,var(--panel-dark) 100%)}
  .services .block--title{top:64px}
  .services .item1{top:196px}
  .services .item2{top:350px}
  .services .item3{top:500px}

  /* inside: who */
  .who .photo--top{top:0;height:160px;background:linear-gradient(135deg,#4a5566,#232831)}
  .who .photo--bottom{bottom:0;height:250px;background:linear-gradient(160deg,#5d6a7c,#1f2630 70%)}
  .who svg{position:absolute;left:0;width:100%}
  .who .block--title{top:190px}
  .who .block--text{top:268px}

  /* inside: team */
  .team .block--title{top:170px}
  .team .block--text{top:270px}
  .team .photo{bottom:0;height:270px;background:linear-gradient(180deg,#39424f,#1e232b)}
  .team svg{position:absolute;left:0;bottom:0;width:100%}

  /* outside: customers */
  .customers{background:var(--panel-mid)}
  .customers .heading{color:#8fb4f2;font-weight:600}
  .customers .block--title{top:70px}
  .customer-list{position:absolute;left:32px;top:190px;display:flex;flex-direction:column;gap:22px}
  .customer{display:flex;align-items:center;gap:8px;font-family:"Montserrat",Arial,sans-serif;font-weight:700;font-size:18px;color:var(--text-light)}
  .customer i{display:block;width:16px;height:16px;background:var(--blue-bright)}
  .customers .photo{bottom:0;height:150px;background:linear-gradient(180deg,#2a3a55,#101318)}

  /* outside: contact */
  .contact .card{position:absolute;left:24px;right:24px;top:34px;height:236px;background:var(--card);padding:22px 22px}
  .contact .heading{font-size:24px;font-weight:600}
  .contact-list{list-style:none;margin-top:20px;display:flex;flex-direction:column;gap:14px}
  .contact-list li{display:flex;align-items:center;gap:10px;font-size:11px;color:var(--text-soft)}
  .contact-list svg{flex:none}
  .contact .photo{top:290px;bottom:0;background:linear-gradient(180deg,#2f4a7a 0%,#1b2638 55%,#0f1218 100%)}

  /* outside: cover */
  .cover{background:linear-gradient(180deg,var(--blue) 0%,var(--blue-deep) 100%)}
  .brand{position:absolute;top:110px;left:0;right:0;display:flex;justify-content:center;align-items:center;gap:10px;font-family:"Montserrat",Arial,sans-serif;font-weight:600;font-size:40px;color:var(--text-light)}
  .brand i{display:block;width:18px;height:18px;border-radius:50%;background:var(--text-light)}
  .tagline{position:absolute;top:190px;left:40px;right:40px;text-align:center;font-family:"Montserrat",Arial,sans-serif;font-size:15px;line-height:1.45;letter-spacing:1px;color:#cfe0ff;text-transform:uppercase}
  .cover .photo{top:380px;bottom:0;background:linear-gradient(180deg,#4a5f86 0%,#22304a 50%,#0e1626 100%)}
</style>
</head>
<body>

<section class="spread spread--inside">
  <article class="panel services">
    <div class="photo" role="img" aria-label="Faded photo of a modern office interior"></div>
    <div class="block block--title"><h2 class="heading">Our<br>Services</h2><span class="heading-bar"></span></div>
    <div class="block item1">
      <p class="sub">Load &amp; Performance Testing</p>
      <p class="body">We test applications under realistic load to ensure speed, stability and scalability of your IT systems and digital services. Bottlenecks are found early and fixed before your users ever notice them in production.</p>
    </div>
    <div class="block item2">
      <p class="sub">Application Performance Monitoring</p>
      <p class="body">Follow the experience of every real user and every transaction. We set up monitoring that makes problems visible at once and gives your teams the data to act on time.</p>
    </div>
    <div class="block item3">
      <p class="sub">Training &amp; Consulting</p>
      <p class="body">Share our knowledge of performance testing tools and monitoring platforms. We support you in building your own performance team, with clear methods, proven tooling and hands-on coaching.</p>
    </div>
  </article>

  <article class="panel who">
    <div class="photo photo--top" role="img" aria-label="Photo of a server room"></div>
    <svg style="top:0" height="170" viewBox="0 0 349 170" preserveAspectRatio="none" aria-hidden="true">
      <polygon points="0,0 140,0 70,90" fill="#2456b5" opacity=".85"/>
      <polygon points="200,0 349,0 349,120" fill="#3d7ee6" opacity=".7"/>
      <polygon points="0,170 349,120 349,170" fill="#1b1d22"/>
    </svg>
    <div class="block block--title"><h2 class="heading">Who<br>we are ?</h2><span class="heading-bar"></span></div>
    <div class="block block--text">
      <p class="body">velnova is a young company in the very specialized area of performance engineering. Whether performance tests or application monitoring, we bring experience from many industries and projects. Our team works closely with your developers and operations staff so results are clear, fast and useful. We are based in Vienna and serve clients across Europe.</p>
    </div>
    <div class="photo photo--bottom" role="img" aria-label="Photo of a network operations control room"></div>
    <svg style="bottom:0" height="250" viewBox="0 0 349 250" preserveAspectRatio="none" aria-hidden="true">
      <polygon points="0,0 349,0 0,70" fill="#1b1d22"/>
      <polygon points="0,250 0,140 150,250" fill="#2456b5" opacity=".85"/>
      <polygon points="349,250 349,90 220,250" fill="#3d7ee6" opacity=".7"/>
    </svg>
  </article>

  <article class="panel team">
    <div class="block block--title"><h2 class="heading">About<br>our team</h2><span class="heading-bar"></span></div>
    <div class="block block--text">
      <p class="body">Our performance engineers guide our customers through the whole process, from first idea to finished report. They combine deep technical skill with a practical view of business needs, and they stay with you until the results are in place and working well for every user.</p>
    </div>
    <div class="photo" role="img" aria-label="Photo of a city skyline at dusk"></div>
    <svg height="270" viewBox="0 0 349 270" preserveAspectRatio="none" aria-hidden="true">
      <polygon points="0,0 349,0 0,60" fill="#1b1d22"/>
      <polygon points="349,0 349,130 200,0" fill="#2456b5" opacity=".8"/>
    </svg>
  </article>
</section>

<section class="spread spread--outside">
  <article class="panel customers">
    <div class="block block--title"><h2 class="heading">Valued<br>Customers</h2></div>
    <div class="customer-list">
      <span class="customer"><i></i>Norvex</span>
      <span class="customer"><i></i>Bellgraf</span>
      <span class="customer"><i></i>Ardena</span>
      <span class="customer"><i></i>Quilta</span>
      <span class="customer"><i></i>Wekora</span>
    </div>
    <div class="photo" role="img" aria-label="Photo of a city skyline at night"></div>
  </article>

  <article class="panel contact">
    <div class="card">
      <h2 class="heading">Contact</h2>
      <ul class="contact-list">
        <li><svg width="16" height="16" viewBox="0 0 16 16"><circle cx="8" cy="8" r="8" fill="#3d7ee6"/><path d="M5.5 4.5l1.5 1.5-1 1a5 5 0 0 0 3 3l1-1 1.5 1.5-1 1c-2.5 0-6-3.5-6-6z" fill="#fff"/></svg>+43 1 555 0190 2040</li>
        <li><svg width="16" height="16" viewBox="0 0 16 16"><circle cx="8" cy="8" r="8" fill="#3d7ee6"/><rect x="4" y="5" width="8" height="6" fill="none" stroke="#fff"/><path d="M4 5l4 3 4-3" fill="none" stroke="#fff"/></svg>office@velnova-ops.com</li>
        <li><svg width="16" height="16" viewBox="0 0 16 16"><circle cx="8" cy="8" r="8" fill="#3d7ee6"/><circle cx="8" cy="8" r="4" fill="none" stroke="#fff"/><path d="M4 8h8M8 4v8" stroke="#fff"/></svg>www.velnova-ops.com</li>
        <li><svg width="16" height="16" viewBox="0 0 16 16"><circle cx="8" cy="8" r="8" fill="#3d7ee6"/><path d="M8 3.5a3 3 0 0 1 3 3c0 2.2-3 6-3 6s-3-3.8-3-6a3 3 0 0 1 3-3z" fill="#fff"/></svg>velnova IT-Services GmbH</li>
      </ul>
    </div>
    <div class="photo" role="img" aria-label="Photo of a glass office tower at night"></div>
  </article>

  <article class="panel cover">
    <div class="brand"><i></i>velnova</div>
    <p class="tagline">Your service provider<br>for application<br>performance</p>
    <div class="photo" role="img" aria-label="Photo of a modern city skyline with light trails"></div>
  </article>
</section>

</body>
</html>
```